Double caffeinated coffee label design

We need to design labels for a new coffee brand. The label size: 2.75” x 4.125” (Corners slightly rounded). There will be front and back label in stickers to be put on standardized bags. Our product is roasted whole bean and ground coffee in 12oz bags. It is described as "strong, bold, intense, and double caffeinated. The product is designed for passionate coffee drinkers who want strong, more caffeinated but not bitter coffee. The coffee is suitable for espresso base coffees.
Target Market(s)
Groceries, food stores, super markets. Heavy and sophisticated coffee drinkers.
Requirements
Must have
- Modern, minimalist style. Strong and bold look. Creative. Impressive.
Nice to have
- Some impressed coffee label designs for reference: https://www.vistrelo.net/find?q=most+impressive+coffee+brand+designs&src=menu&mode=img&ref=X&key=7hQpLmZrT2wXvBn4KcYsDfGaJuEo9RtMiHb3NqVe&w=1280&h=610#pic=kR4mTwXzNpQbLs:

```html
<!DOCTYPE html>
<html lang="en">
<head>
<meta charset="utf-8">
<title>Torvik Coffee – Label</title>
<link rel="stylesheet" href="https://fonts.googleapis.com/css2?family=Berkshire+Swash&family=Josefin+Sans:wght@400;600&family=Oswald:wght@500&display=swap">
<style>
  :root {
    --backdrop: #f5f3ee;
    --kraft-light: #dcbf93;
    --kraft-mid: #cfae7f;
    --kraft-dark: #c19c6b;
    --kraft-glow: rgba(236, 214, 176, 0.55);
    --ink: #2b2522;
    --roast: #4a1f14;
    --bean: #5a2418;
  }
  html, body {
    margin: 0;
    width: 1164px;
    height: 1200px;
    overflow: hidden;
    background: var(--backdrop);
  }
  .label {
    position: absolute;
    left: 212px;
    top: 45px;
    width: 740px;
    height: 1110px;
    border-radius: 34px;
    background: linear-gradient(160deg, var(--kraft-light) 0%, var(--kraft-mid) 55%, var(--kraft-dark) 100%);
    overflow: hidden;
  }
  .brand {
    position: absolute;
    left: 0; right: 0;
    top: 160px;
    text-align: center;
    font-family: "Josefin Sans", sans-serif;
    font-weight: 600;
    font-size: 104px;
    line-height: 1;
    color: var(--roast);
  }
  .brand-sub {
    position: absolute;
    left: 0; right: 0;
    top: 285px;
    text-align: center;
    font-family: "Josefin Sans", sans-serif;
    font-weight: 400;
    font-size: 32px;
    letter-spacing: 7px;
    color: var(--ink);
  }
  .burst {
    position: absolute;
    left: 20px;
    top: 350px;
    width: 700px;
    height: 500px;
    border-radius: 50%;
    background: radial-gradient(ellipse at center, var(--kraft-glow) 0%, rgba(236, 214, 176, 0) 70%);
  }
  .title {
    position: absolute;
    left: 0; right: 0;
    text-align: center;
    font-family: "Berkshire Swash", cursive;
    color: var(--ink);
    line-height: 1;
    margin: 0;
    font-weight: 400;
  }
  .title-roasted { top: 405px; font-size: 74px; }
  .title-whole { top: 492px; font-size: 74px; }
  .title-amp { top: 568px; font-size: 44px; }
  .title-ground { top: 620px; font-size: 78px; }
  .ornament {
    position: absolute;
    left: 243px;
    top: 722px;
    width: 255px;
    height: 40px;
    border-radius: 20px;
    background: var(--kraft-dark);
  }
  .beans {
    position: absolute;
    left: 323px;
    top: 800px;
    width: 94px;
    height: 96px;
    border-radius: 40px;
    background: var(--bean);
    opacity: .85;
  }
  .tagline {
    position: absolute;
    left: 0; right: 0;
    text-align: center;
    font-family: "Oswald", sans-serif;
    font-weight: 500;
    font-size: 23px;
    letter-spacing: 2px;
    color: var(--ink);
  }
  .tagline-traits { top: 934px; }
  .tagline-strength { top: 974px; letter-spacing: 3px; }
</style>
</head>
<body>
  <main class="label">
    <div class="brand">Torvik</div>
    <div class="brand-sub">COFFEE</div>

    <div class="burst" role="img" aria-label="Decorative sunburst rays radiating around the product name"></div>

    <h1 class="title title-roasted">Roasted</h1>
    <p class="title title-whole">Whole Bean</p>
    <p class="title title-amp">&amp;</p>
    <p class="title title-ground">Ground Coffee</p>

    <div class="ornament" role="img" aria-label="Decorative swirl flourish under the product name"></div>
    <div class="beans" role="img" aria-label="Illustration of three roasted coffee beans"></div>

    <div class="tagline tagline-traits">STRONG | BOLD | INTENSE</div>
    <div class="tagline tagline-strength">DOUBLE CAFFEINATED</div>
  </main>
</body>
</html>
```